Business Cards Needed For Veterinary Business

Looking for a business card design for a veterinary blood bank. We would like it to be clean and professional on appearance but still warm and inviting. We would like to utilize our logo and similar coloring. We will use our phone number, email, website, employee name, employee title.

We do not want a bunch of animated animal photos but do not need the style to be as clinical as a laboratory or human medical procedure office.

We are looking for some creative ideas to choose from so that we can generate a standout professional business card for our management team to utilize.

Target Market(s)

professionals

Industry/Entity Type

veterinary

Contact Information for Business Card

employee name, employee title, phone number, website URL, email

Font styles to use
Sans Serif

Colors
0054AA
0677BA
7BADD7
CADEEF
E8F1F8
EB3D1F
EC4F4E
F09395
F8D3D4
FCEDEE

Requirements
Nice to have
• creative design
Should not have
• animated photos

```html
<!DOCTYPE html>
<html lang="en">
<head>
<meta charset="utf-8">
<title>Corvale Animal Donor Center – Business Card</title>
<link href="https://fonts.googleapis.com/css2?family=Montserrat:wght@400;500;700;800&display=swap" rel="stylesheet">
<style>
  :root{
    --bg:#3d3d3d;
    --card-white:#ffffff;
    --brand-red:#e81c25;
    --brand-red-deep:#cc1119;
    --brand-blue:#1c4a96;
    --text-grey:#6b6b6b;
    --text-dark:#444444;
    --rule-grey:#d6d6d6;
  }
  *{box-sizing:border-box;margin:0;padding:0}
  html,body{width:1200px;height:803px;overflow:hidden;background:var(--bg);font-family:"Montserrat",sans-serif}
  .stage{position:relative;width:1200px;height:803px}
  .card{position:absolute;top:250px;width:520px;height:300px;border-radius:18px;overflow:hidden;box-shadow:0 14px 30px rgba(0,0,0,.35)}

  /* front */
  .card--front{left:50px;background:var(--card-white)}
  .brand{position:absolute;display:flex;align-items:center;gap:10px;white-space:nowrap}
  .card--front .brand{top:38px;right:34px}
  .brand-dot{width:26px;height:26px;border-radius:50%;background:var(--brand-red);flex:none}
  .brand-text{color:var(--brand-red);font-weight:700;line-height:1}
  .brand-name{font-size:30px;letter-spacing:3px}
  .brand-tagline{font-size:9.5px;letter-spacing:1.6px;margin-top:6px}
  .rule{position:absolute;left:34px;right:34px;top:118px;height:1px;background:var(--rule-grey)}
  .person{position:absolute;left:34px;top:150px}
  .person-name{color:var(--brand-red);font-weight:800;font-size:22px;letter-spacing:1px}
  .person-title{color:var(--text-grey);font-size:12px;margin-top:4px}
  .contact{position:absolute;left:34px;top:212px;list-style:none;border-top:1px solid var(--rule-grey);padding-top:8px;width:210px}
  .contact li{display:flex;align-items:center;gap:8px;color:var(--text-dark);font-size:13px;line-height:19px;white-space:nowrap}
  .contact svg{width:11px;height:11px;fill:var(--brand-blue);flex:none}
  .band{position:absolute;left:0;bottom:0;width:100%;height:60px}
  .band-url{position:absolute;right:20px;bottom:13px;color:#fff;font-size:12px;font-weight:500;white-space:nowrap}

  /* back */
  .card--back{left:630px;background:var(--brand-red)}
  .card--back .brand{top:96px;left:50%;transform:translateX(-50%);gap:14px}
  .card--back .brand-dot{width:40px;height:40px;background:var(--brand-red-deep)}
  .card--back .brand-text{color:var(--brand-red-deep)}
  .card--back .brand-name{font-size:44px;letter-spacing:4px}
  .card--back .brand-tagline{font-size:12px;letter-spacing:2px}
  .back-url{position:absolute;left:0;right:0;bottom:58px;text-align:center;color:#fff;font-size:14px;font-weight:500}
</style>
</head>
<body>
<main class="stage">
  <section class="card card--front" aria-label="Card front">
    <div class="brand">
      <span class="brand-dot"></span>
      <div class="brand-text">
        <div class="brand-name">CORVALE</div>
        <div class="brand-tagline">ANIMAL DONOR CENTER</div>
      </div>
    </div>
    <div class="rule"></div>
    <div class="person">
      <div class="person-name">JORDAN LEE</div>
      <div class="person-title">President</div>
    </div>
    <ul class="contact">
      <li><svg viewBox="0 0 24 24"><path d="M6.6 10.8a15 15 0 0 0 6.6 6.6l2.2-2.2c.3-.3.7-.4 1-.2 1.1.4 2.3.6 3.6.6.6 0 1 .4 1 1V20c0 .6-.4 1-1 1A17 17 0 0 1 3 4c0-.6.4-1 1-1h3.5c.6 0 1 .4 1 1 0 1.3.2 2.5.6 3.6.1.3 0 .7-.2 1z"/></svg>555-014-2200</li>
      <li><svg viewBox="0 0 24 24"><path d="M2 5h20v14H2zm2 2v.5l8 5 8-5V7z"/></svg>hello@corvale-demo.com</li>
    </ul>
    <svg class="band" viewBox="0 0 520 60" preserveAspectRatio="none">
      <path d="M0 40 H320 L330 50 H0 Z" fill="var(--brand-blue)"/>
      <path d="M0 52 H332 L326 46 L336 22 H520 V60 H0 Z" fill="var(--brand-red)"/>
    </svg>
    <div class="band-url">www.corvale-demo.com</div>
  </section>

  <section class="card card--back" aria-label="Card back">
    <div class="brand">
      <span class="brand-dot"></span>
      <div class="brand-text">
        <div class="brand-name">CORVALE</div>
        <div class="brand-tagline">ANIMAL DONOR CENTER</div>
      </div>
    </div>
    <div class="back-url">www.corvale-demo.com</div>
  </section>
</main>
</body>
</html>
```